Banner dimension 1767 X 887 for Tolvenko website

Need one banner for our website www.tolvenko.com.au, The dimension of the banner should be 1767 x 887. Attached to this brief are two images that needs to be on that one banner, PLEASE DO NOT SEND SEPARATE BANNERS, both images on the same banner. Thanks

The banner should have the following message on it:

1.) " Take a further 40% off all stock" ( use code: TOLVENKO. Ends 31/12/2015)
2.) " Kick back or kick it up a notch this Autumn in the most versatile pique striped polo shirts and Pinafore belt strap denim dress"

Target Market(s)

kids aged 5-12yrs

Requirements
Must have
• very playful

```html
<!DOCTYPE html>
<html lang="en">
<head>
<meta charset="utf-8">
<title>Tolvenko Summer Sale Banner</title>
<link rel="stylesheet" href="https://fonts.googleapis.com/css2?family=Archivo+Black&display=swap">
<style>
  :root {
    --page: #ffffff;
    --dot: #c6c6c6;
    --orange: #f57f20;
    --lime: #d5e60b;
    --blue: #0497e8;
    --pink: #e31b56;
    --ink: #333333;
    --olive: #2f3f0c;
    --white: #ffffff;
  }
  html, body {
    margin: 0;
    width: 1200px;
    height: 1000px;
    overflow: hidden;
    background: var(--page);
  }
  .canvas {
    position: relative;
    width: 1200px;
    height: 1000px;
  }
  .banner {
    position: absolute;
    left: 38px;
    top: 201px;
    width: 1132px;
    height: 568px;
    background: var(--page);
    border: 1px solid #9a9a9a;
    box-shadow: 3px 4px 4px rgba(0,0,0,0.55);
    overflow: hidden;
    font-family: "Archivo Black", "Arial Black", sans-serif;
  }
  .layer {
    position: absolute;
    left: 0;
    top: 0;
  }
  .photo {
    position: absolute;
  }
  .photo-boy {
    left: 50px;
    top: 28px;
    width: 250px;
    height: 530px;
    border-radius: 90px 90px 30px 30px;
    background: linear-gradient(180deg, #6b4a35 0%, #3f6a4c 22%, #2f4f3a 45%, #9bb2c6 60%, #d9b299 80%, #2a2a2a 100%);
  }
  .photo-girl {
    left: 890px;
    top: 4px;
    width: 236px;
    height: 564px;
    border-radius: 100px 100px 16px 16px;
    background: linear-gradient(180deg, #4a2e22 0%, #f1f1f1 22%, #3e6b8c 38%, #5d87a6 70%, #e2b9a3 88%, #d7ad97 100%);
  }
  .line {
    position: absolute;
    margin: 0;
    white-space: nowrap;
    line-height: 1;
  }
  .offer {
    left: 350px;
    top: 78px;
    font-size: 29px;
    color: var(--ink);
    transform: rotate(-1.8deg);
    transform-origin: left center;
  }
  .offer .big { font-size: 50px; }
  .code {
    left: 266px;
    top: 162px;
    font-size: 29px;
    color: var(--ink);
    transform: rotate(1.3deg);
    transform-origin: left center;
  }
  .code .ends { font-size: 22px; margin-left: 10px; }
  .tagline {
    font-size: 31px;
    color: var(--olive);
    transform: rotate(-1.6deg);
    transform-origin: left center;
  }
  .tagline-1 { left: 281px; top: 240px; }
  .tagline-2 { left: 292px; top: 278px; }
  .tagline .season { font-size: 45px; }
  .product {
    font-size: 30px;
    color: var(--white);
  }
  .product-polo {
    left: 345px;
    top: 320px;
    transform: rotate(1.6deg);
    transform-origin: left center;
    line-height: 1.35;
    white-space: normal;
  }
  .product-dress {
    right: 270px;
    top: 434px;
    text-align: right;
    transform: rotate(1.8deg);
    transform-origin: right center;
    line-height: 1.3;
    white-space: normal;
  }
</style>
</head>
<body>
<div class="canvas">
  <section class="banner" aria-label="Tolvenko summer sale banner">
    <svg class="layer dots" width="1132" height="568" viewBox="0 0 1132 568" aria-hidden="true">
      <g fill="var(--dot)">
        <circle cx="465" cy="57" r="44"/>
        <circle cx="868" cy="-12" r="62"/>
        <circle cx="47" cy="177" r="37"/>
        <circle cx="193" cy="348" r="77"/>
        <circle cx="40" cy="423" r="28"/>
        <circle cx="422" cy="575" r="51"/>
        <circle cx="845" cy="385" r="58"/>
        <circle cx="1099" cy="534" r="25"/>
      </g>
    </svg>

    <div class="photo photo-boy" role="img" aria-label="Photo of a smiling boy in a green striped pique polo shirt and denim cargo shorts, posing playfully"></div>

    <svg class="layer bands" width="1132" height="568" viewBox="0 0 1132 568" aria-hidden="true">
      <polygon fill="var(--orange)" points="337,80 939,60 942,132 340,149"/>
      <polygon fill="var(--lime)" points="238,140 850,155 868,235 262,199"/>
      <polygon fill="var(--blue)" points="288,316 800,323 786,433 294,397"/>
      <polygon fill="var(--pink)" points="407,411 886,435 874,519 447,519"/>
    </svg>

    <div class="photo photo-girl" role="img" aria-label="Photo of a smiling girl with long hair wearing a white tee under a pinafore belt strap denim dress"></div>

    <p class="line offer">Take a further <span class="big">40%</span> off all stock</p>
    <p class="line code">use code: TOLVENKO <span class="ends">Ends 31/12/2015</span></p>
    <p class="line tagline tagline-1">KICK BACK OR KICK IT</p>
    <p class="line tagline tagline-2">UP A NOTCH THIS <span class="season">SUMMER</span> IN</p>
    <p class="line product product-polo">The most versatile<br>Pique Striped Polo Shirts</p>
    <p class="line product product-dress">Pinafore Belt Strap<br>Denim Dress</p>
  </section>
</div>
</body>
</html>
```